Design home page for brightvane.xyz

We’re seeking a sleek, lead-generation-focused single-page website for Brightvane.xyz that communicates our expertise in delivering high-intent leads to mid-sized businesses. The goal is to guide visitors toward scheduling a free consultation while emphasizing our performance-based approach and comprehensive service offerings.

Industry/Entity Type

Marketing

Number of Pages Required

1 page

Font styles to use
Sans Serif

Requirements
Must have
• content from https://files.quorvalet.example/doc/7hTmwQRZa93KpLdVyxNe42UcBsFoGj8rYiMn5EkPtWz/view?tab=t.0
Nice to have
• color pallet from here https://files.quorvalet.example/doc/4pRkz-NWb62VxLeTyqJs8cHaDmFu3GiYoBnQ5tXeKv/view?tab=t.0

```html
<!DOCTYPE html>
<html lang="en">
<head>
<meta charset="utf-8">
<title>Brightvane.xyz — High-Intent Leads Delivered</title>
<link href="https://fonts.googleapis.com/css2?family=Outfit:wght@600;700;800&family=Poppins:ital,wght@0,400;0,500;0,600;1,400&display=swap" rel="stylesheet">
<style>
:root{
  --backdrop:#dcdcdc;
  --page:#ffffff;
  --teal:#0ab7c8;
  --red:#a0111a;
  --cream:#f6e9c6;
  --dark:#2e2e2e;
  --ink:#1b1b1b;
  --muted:#555555;
  --line:#e4e4e4;
}
*{box-sizing:border-box;margin:0;padding:0}
html,body{width:1200px;height:4317px;overflow:hidden}
body{background:var(--backdrop);font-family:"Poppins",sans-serif;color:var(--ink);position:relative}
.page{position:absolute;left:214px;top:84px;width:772px;height:4148px;background:var(--page)}
.abs{position:absolute}
.heading{font-family:"Outfit",sans-serif;font-weight:700;letter-spacing:-0.035em;line-height:1.05;color:var(--ink)}
.h-section{font-size:29px}
.body{font-size:8.6px;line-height:16px;color:var(--muted)}
.title{font-size:10px;font-weight:600;color:var(--ink)}
.logo{font-family:"Poppins",sans-serif;font-weight:600;font-size:22px;letter-spacing:-0.01em;color:var(--ink);text-align:center;width:100%}

/* hero */
.hero{left:221px;top:131px;width:758px;height:427px;background:var(--teal);border-radius:8px}
.hero-cut{background:var(--page)}
.hero-title{left:263px;top:184px;color:#fff;font-size:58px;line-height:53px}
.hero-text{left:263px;top:420px;width:310px;color:#fff;font-size:8.4px;line-height:16px}
.hero-art{left:612px;top:226px;width:335px;height:226px;border-radius:50% 50% 20px 20px;background:radial-gradient(circle at 50% 45%,#1d4fb0 0%,#2a7bd6 40%,rgba(10,183,200,0) 72%)}
.pill{display:flex;align-items:center;justify-content:space-between;border-radius:40px;font-size:9px}
.pill-red{left:419px;top:523px;width:511px;height:35px;background:var(--red);color:#fff;padding:0 4px 0 14px}
.pill-dark{left:732px;top:4043px;width:198px;height:38px;background:var(--dark);color:#fff;padding:0 4px 0 18px}
.arrow-dot{width:27px;height:27px;border-radius:50%;background:#fff;display:flex;align-items:center;justify-content:center}

/* photos */
.photo{border-radius:5px}

/* service cards */
.card{padding:14px 12px;border-radius:6px}
.card .title{margin:8px 0 8px}
.card-cream{background:var(--cream)}
.card-red{background:var(--red)}
.card-red .title,.card-red .body{color:#fff}
.card-dark{background:var(--dark)}
.card-dark .title,.card-dark .body{color:#fff}
.card .body{font-size:8.2px;line-height:15.5px}

/* lists */
.tick-item{display:flex;gap:12px}
.tick-item .title{margin-bottom:9px}

/* cream content band */
.band{left:221px;top:1849px;width:758px;height:352px;background:var(--cream);border-radius:8px}
.topic{display:flex;align-items:center;gap:12px;font-size:9.5px;font-weight:500;color:var(--ink)}

/* image cards with caption */
.feature-img{border-radius:6px;overflow:hidden}
.feature-img .heading{position:absolute;left:17px;bottom:16px;color:#fff;font-size:27px}

/* testimonials */
.quote-card{background:#fff;border-radius:6px;box-shadow:0 2px 14px rgba(0,0,0,.08);text-align:center;padding:22px 24px}
.quote-card.active{border:1.5px solid var(--red);box-shadow:none}
.avatar{width:34px;height:34px;border-radius:50%;margin:0 auto 10px;background:linear-gradient(#d6b79a,#7a5a44)}
.q-name{font-size:9px;font-weight:600}
.q-role{font-size:6.5px;color:var(--red);margin:4px 0 16px}
.q-text{font-size:8px;line-height:16px;font-style:italic;color:var(--muted)}

/* cta */
.cta{left:221px;top:3776px;width:758px;height:305px;background:var(--red);border-radius:8px}
.cta .heading{color:#fff}
.cta-list .title,.cta-list .body{color:#fff}
</style>
</head>
<body>
<div class="page"></div>

<!-- header -->
<div class="abs logo" style="left:0;top:92px">brightvane.xyz</div>

<!-- hero -->
<div class="abs hero"></div>
<div class="abs hero-cut" style="left:410px;top:511px;width:569px;height:47px;border-top-left-radius:16px"></div>
<div class="abs hero-cut" style="left:938px;top:477px;width:41px;height:36px;border-top-left-radius:14px"></div>
<h1 class="abs heading hero-title">High-Intent<br>Leads Delivered<br>Directly to Your<br>Pipeline</h1>
<p class="abs hero-text">Take the guesswork out of lead generation. We connect you with high-intent prospects who are genuinely interested in what you offer, helping you grow your sales pipeline with ease.</p>
<div class="abs hero-art" role="img" aria-label="Illustration of a lead funnel turning prospects into revenue"></div>
<a class="abs pill pill-red">Let's talk about how we can deliver the leads your business needs. Schedule a Free Call Today
  <span class="arrow-dot"><svg width="11" height="11" viewBox="0 0 12 12"><path d="M3 9L9 3M4 3h5v5" fill="none" stroke="#a0111a" stroke-width="1.3"/></svg></span></a>

<!-- results -->
<h2 class="abs heading h-section" style="left:263px;top:618px">We Deliver Results, Not Promises</h2>
<p class="abs body" style="left:263px;top:662px;width:300px">At Brightvane.xyz, we specialize in providing conversion-ready leads that fuel sustainable business growth.</p>
<div class="abs photo" style="left:263px;top:716px;width:218px;height:129px;background:linear-gradient(135deg,#f1f1f1,#bdbdbd)" role="img" aria-label="Photo of hands typing on a laptop"></div>
<div class="abs photo" style="left:491px;top:716px;width:216px;height:129px;background:linear-gradient(135deg,#e8e2da,#8f8a86)" role="img" aria-label="Photo of a person reviewing charts on a tablet"></div>
<div class="abs photo" style="left:717px;top:716px;width:218px;height:129px;background:linear-gradient(135deg,#3a3a3a,#b9853c)" role="img" aria-label="Photo of a professional using a tablet with data overlays"></div>
<div class="abs" style="left:263px;top:858px;width:200px"><div class="title">Entrepreneur-Led Expertise</div><p class="body" style="margin-top:8px">Founded by seasoned entrepreneurs with proven lead generation success.</p></div>
<div class="abs" style="left:491px;top:858px;width:200px"><div class="title">Performance-Based Model</div><p class="body" style="margin-top:8px">No upfront costs—we succeed only when you do.</p></div>
<div class="abs" style="left:717px;top:858px;width:210px"><div class="title">Comprehensive Approach</div><p class="body" style="margin-top:8px">From SEO to PPC campaigns and high-value content creation, we manage it all.</p></div>

<!-- services -->
<h2 class="abs heading h-section" style="left:263px;top:973px">Comprehensive<br>End-to-End Lead Generation</h2>
<p class="abs body" style="left:263px;top:1052px;width:280px">We handle everything needed to deliver high-quality leads so you can focus on scaling your business.</p>

<div class="abs card card-cream" style="left:776px;top:977px;width:159px;height:127px">
  <svg width="20" height="20" viewBox="0 0 24 24" fill="none" stroke="#a0111a" stroke-width="1.5"><path d="M5 19c1-3 2-4 4-5l5-5c2-2 5-3 6-3 0 1-1 4-3 6l-5 5c-1 2-2 3-5 4z"/><circle cx="15" cy="9" r="1.5"/></svg>
  <div class="title">SEO &amp; Social Media</div><p class="body">Organic strategies to attract quality traffic and generate leads.</p></div>
<div class="abs card card-red" style="left:605px;top:1066px;width:161px;height:129px">
  <svg width="20" height="20" viewBox="0 0 24 24" fill="none" stroke="#fff" stroke-width="1.5"><rect x="4" y="7" width="16" height="13" rx="1"/><path d="M6 4h12M4 11h16"/></svg>
  <div class="title">Design &amp; Development</div><p class="body">Professional assets and optimized landing pages for maximum engagement.</p></div>
<div class="abs card card-dark" style="left:776px;top:1116px;width:159px;height:129px">
  <svg width="20" height="20" viewBox="0 0 24 24" fill="none" stroke="#fff" stroke-width="1.5"><path d="M3 3v18h18M6 16l5-5 3 3 6-7"/></svg>
  <div class="title">Real-Time Optimization</div><p class="body">Ongoing analysis and adjustments for peak performance and ROI.</p></div>
<div class="abs card card-cream" style="left:434px;top:1138px;width:161px;height:129px">
  <svg width="20" height="20" viewBox="0 0 24 24" fill="none" stroke="#a0111a" stroke-width="1.5"><path d="M6 3h8l4 4v14H6z M14 3v4h4"/></svg>
  <div class="title">Content Creation</div><p class="body">High-value gated content, articles, and blog posts to attract and convert leads.</p></div>
<div class="abs card card-cream" style="left:605px;top:1207px;width:161px;height:129px">
  <svg width="20" height="20" viewBox="0 0 24 24" fill="none" stroke="#a0111a" stroke-width="1.5"><path d="M4 4l15 6-6 2-2 6z M13 12l6 6"/></svg>
  <div class="title">PPC Campaigns</div><p class="body">Targeted paid search to drive qualified leads.</p></div>

<!-- why choose -->
<div class="abs feature-img" style="left:263px;top:1411px;width:275px;height:322px;background:linear-gradient(160deg,#17b0c6 0%,#0b6f86 50%,#062f3c 100%)" role="img" aria-label="Image of a yellow plane breaking away from a line of grey planes">
  <div class="heading">Why Choose<br>Brightvane.xyz?</div></div>
<p class="abs body" style="left:263px;top:1747px;width:250px">We specialize in delivering high-intent leads that drive measurable growth. Here's how we stand out</p>

<div class="abs" style="left:578px;top:1455px;width:360px">
  <div class="tick-item"><svg width="15" height="15" viewBox="0 0 16 16"><circle cx="8" cy="8" r="7" fill="none" stroke="#a0111a" stroke-width="1.2"/><path d="M5 8.2l2 2 4-4" fill="none" stroke="#a0111a" stroke-width="1.2"/></svg>
    <div><div class="title">Results-Driven Approach</div><p class="body">We handle all aspects of lead generation, from creating lead magnets to executing advertising and SEO campaigns, delivering high-quality leads that align with your goals.</p></div></div>
  <div class="tick-item" style="margin-top:33px"><svg width="15" height="15" viewBox="0 0 16 16"><circle cx="8" cy="8" r="7" fill="none" stroke="#a0111a" stroke-width="1.2"/><path d="M5 8.2l2 2 4-4" fill="none" stroke="#a0111a" stroke-width="1.2"/></svg>
    <div><div class="title">Tailored Strategies</div><p class="body">Our campaigns are designed to connect you with prospects who are genuinely interested in the type of products or services you offer.</p></div></div>
  <div class="tick-item" style="margin-top:33px"><svg width="15" height="15" viewBox="0 0 16 16"><circle cx="8" cy="8" r="7" fill="none" stroke="#a0111a" stroke-width="1.2"/><path d="M5 8.2l2 2 4-4" fill="none" stroke="#a0111a" stroke-width="1.2"/></svg>
    <div><div class="title">Simplified Growth Solutions</div><p class="body">With all the heavy lifting managed by our team, you can focus entirely on growing your business and closing more deals.</p></div></div>
</div>

<!-- tailored content band -->
<div class="abs band"></div>
<div class="abs" style="left:851px;top:2159px;width:128px;height:42px;background:var(--page);border-top-left-radius:16px"></div>
<h2 class="abs heading h-section" style="left:263px;top:1910px">Tailored Content for High-Intent Lead Capture</h2>
<p class="abs body" style="left:263px;top:1953px">We create custom-crafted content tailored for your audience</p>
<div class="abs topic" style="left:263px;top:2006px"><svg width="18" height="18" viewBox="0 0 24 24" fill="none" stroke="#a0111a" stroke-width="1.5"><path d="M5 4h12v16H5z M8 4v16"/></svg>Guides and eBooks</div>
<div class="abs topic" style="left:471px;top:2006px"><svg width="18" height="18" viewBox="0 0 24 24" fill="none" stroke="#a0111a" stroke-width="1.5"><path d="M3 18a9 9 0 0118 0z M12 18l4-6"/></svg>Industry Insights Reports</div>
<div class="abs topic" style="left:672px;top:2006px"><svg width="18" height="18" viewBox="0 0 24 24" fill="none" stroke="#a0111a" stroke-width="1.5"><circle cx="12" cy="7" r="3"/><circle cx="6" cy="17" r="3"/><circle cx="18" cy="17" r="3"/></svg>Infographics &amp; Visual Guides</div>
<div class="abs topic" style="left:263px;top:2056px"><svg width="18" height="18" viewBox="0 0 24 24" fill="none" stroke="#a0111a" stroke-width="1.5"><circle cx="12" cy="12" r="9"/><path d="M9.5 9.5a2.5 2.5 0 115 0c0 2-2.5 2-2.5 4M12 17v.5"/></svg>Glossary of Industry Terms</div>
<div class="abs topic" style="left:471px;top:2056px"><svg width="18" height="18" viewBox="0 0 24 24" fill="none" stroke="#a0111a" stroke-width="1.5"><path d="M4 6h1M4 12h1M4 18h1M9 6h11M9 12h11M9 18h11"/></svg>Checklist for Best Practices</div>
<div class="abs topic" style="left:672px;top:2056px"><svg width="18" height="18" viewBox="0 0 24 24" fill="none" stroke="#a0111a" stroke-width="1.5"><path d="M3 12a9 9 0 0118 0zM12 12v7a2 2 0 01-4 0"/></svg>Trend Spotting Forecast</div>
<div class="abs topic" style="left:263px;top:2108px"><svg width="18" height="18" viewBox="0 0 24 24" fill="none" stroke="#a0111a" stroke-width="1.5"><rect x="3" y="5" width="18" height="14"/><path d="M3 16l5-5 4 4 3-3 6 6"/></svg>Templates and Toolkits</div>
<div class="abs topic" style="left:471px;top:2108px"><svg width="18" height="18" viewBox="0 0 24 24" fill="none" stroke="#a0111a" stroke-width="1.5"><circle cx="12" cy="12" r="9"/><path d="M15 9l-2 4-4 2 2-4z"/></svg>Competitive Landscape</div>
<div class="abs topic" style="left:672px;top:2108px"><svg width="18" height="18" viewBox="0 0 24 24" fill="none" stroke="#a0111a" stroke-width="1.5"><rect x="3" y="5" width="18" height="14" rx="1"/><path d="M7 10h10M7 14h6"/></svg>Whitepapers</div>

<!-- how we deliver -->
<div class="abs" style="left:263px;top:2318px;width:370px">
  <div class="tick-item"><svg width="15" height="15" viewBox="0 0 16 16"><circle cx="8" cy="8" r="7" fill="none" stroke="#a0111a" stroke-width="1.2"/><path d="M5 8.2l2 2 4-4" fill="none" stroke="#a0111a" stroke-width="1.2"/></svg>
    <div><div class="title">Precise Market Targeting</div><p class="body">We start by understanding your ideal customer profile and identifying high-intent prospects in your market.</p></div></div>
  <div class="tick-item" style="margin-top:33px"><svg width="15" height="15" viewBox="0 0 16 16"><circle cx="8" cy="8" r="7" fill="none" stroke="#a0111a" stroke-width="1.2"/><path d="M5 8.2l2 2 4-4" fill="none" stroke="#a0111a" stroke-width="1.2"/></svg>
    <div><div class="title">Customized Campaign Execution</div><p class="body">We take the time to understand your audience, creating and running campaigns tailored to their interests, leveraging insights from advertising, SEO, and lead magnets.</p></div></div>
  <div class="tick-item" style="margin-top:33px"><svg width="15" height="15" viewBox="0 0 16 16"><circle cx="8" cy="8" r="7" fill="none" stroke="#a0111a" stroke-width="1.2"/><path d="M5 8.2l2 2 4-4" fill="none" stroke="#a0111a" stroke-width="1.2"/></svg>
    <div><div class="title">All-Inclusive Management</div><p class="body">From strategy to execution, we handle every detail, delivering leads while you focus on closing deals.</p></div></div>
</div>
<div class="abs feature-img" style="left:662px;top:2273px;width:273px;height:323px;background:linear-gradient(160deg,#5a6a78 0%,#20262c 45%,#050607 100%)" role="img" aria-label="Photo of a finger pressing a glowing generate leads key">
  <div class="heading">How We Deliver<br>High-Quality<br>Leads</div></div>
<p class="abs body" style="left:662px;top:2608px;width:230px">Our streamlined process ensures you receive ready-to-engage leads without the hassle</p>

<!-- sets us apart -->
<h2 class="abs heading h-section" style="left:263px;top:2712px">What Sets Us Apart?</h2>
<p class="abs body" style="left:263px;top:2757px;width:290px">We're more than just a lead generation service—our approach ensures valuable opportunities for your business</p>
<div class="abs photo" style="left:263px;top:2811px;width:218px;height:127px;background:linear-gradient(135deg,#dfe6f0,#8fa6c4)" role="img" aria-label="Photo of a magnet attracting people icons"></div>
<div class="abs photo" style="left:491px;top:2811px;width:216px;height:127px;background:linear-gradient(135deg,#e8e8e8,#6d6d6d)" role="img" aria-label="Photo of a smiling professional at an office desk"></div>
<div class="abs photo" style="left:717px;top:2811px;width:218px;height:127px;background:linear-gradient(135deg,#c9ccd1,#3e4249)" role="img" aria-label="Photo of two business people shaking hands"></div>
<div class="abs" style="left:263px;top:2953px;width:200px"><div class="title">High-Intent Leads</div><p class="body" style="margin-top:8px">The high-intent leads we generate provide a solid starting point for building meaningful connections.</p></div>
<div class="abs" style="left:491px;top:2953px;width:200px"><div class="title">Complete Service</div><p class="body" style="margin-top:8px">We take care of everything needed to generate leads, so you can stay focused on growing your business.</p></div>
<div class="abs" style="left:717px;top:2953px;width:210px"><div class="title">Success-Based Partnership</div><p class="body" style="margin-top:8px">With our results-driven model, you pay only for the leads we deliver, ensuring value every step of the way.</p></div>

<!-- effortless growth -->
<div class="abs card card-cream" style="left:263px;top:3102px;width:159px;height:161px">
  <svg width="24" height="24" viewBox="0 0 24 24" fill="none" stroke="#a0111a" stroke-width="1.5"><path d="M4 9h4a2 2 0 114 0h4v4a2 2 0 110 4v4H4v-4a2 2 0 100-4z"/></svg>
  <div class="title">Hands-Off Convenience</div><p class="body">We manage the strategy, content, advertising, and optimization, delivering a steady flow of high-quality prospects.</p></div>
<h2 class="abs heading h-section" style="left:440px;top:3102px;width:320px;text-align:center;line-height:30px">Effortless<br>Growth,<br>Designed for<br>You</h2>
<p class="abs body" style="left:490px;top:3236px;width:220px;text-align:center">We simplify lead generation, so you can focus on growing your business</p>
<div class="abs card card-red" style="left:776px;top:3102px;width:159px;height:161px">
  <svg width="24" height="24" viewBox="0 0 24 24" fill="none" stroke="#fff" stroke-width="1.5"><path d="M4 10a8 8 0 0114-4l2 2M20 4v4h-4M20 14a8 8 0 01-14 4l-2-2M4 20v-4h4"/></svg>
  <div class="title">Built to Scale</div><p class="body">Our process adapts to your growth goals, ensuring consistent lead flow whether you're starting small or scaling rapidly.</p></div>

<!-- testimonials -->
<div class="abs" style="left:262px;top:3300px;font-family:'Outfit',sans-serif;font-weight:800;font-size:260px;line-height:260px;color:#efefef" aria-hidden="true">&ldquo;</div>
<h2 class="abs heading h-section" style="left:0;width:1200px;text-align:center;top:3347px">Proven Success Stories</h2>
<p class="abs body" style="left:0;width:1200px;text-align:center;top:3392px;font-size:8px">Discover how our clients have achieved exceptional growth with Brightvane.xyz</p>

<div class="abs quote-card" style="left:288px;top:3468px;width:190px;height:219px">
  <div class="avatar" role="img" aria-label="Client portrait"></div>
  <div class="q-name">Rowan T.</div><div class="q-role">VP of Sales at a Mid-Sized B2B Firm</div>
  <p class="q-text">"Brightvane.xyz has completely transformed our lead generation efforts. We've seen a 35% increase in high-quality leads in just three months."</p></div>
<div class="abs quote-card active" style="left:491px;top:3451px;width:218px;height:250px">
  <div class="avatar" style="width:42px;height:42px" role="img" aria-label="Client portrait"></div>
  <div class="q-name">Priya K.</div><div class="q-role">CEO of a Professional Services Company</div>
  <p class="q-text" style="font-size:8.4px;line-height:17px">"The team at Brightvane.xyz took care of everything—from content to campaigns. Their performance-based model meant we only paid when results came in. It's a win-win!"</p></div>
<div class="abs quote-card" style="left:721px;top:3468px;width:192px;height:219px">
  <div class="avatar" role="img" aria-label="Client portrait"></div>
  <div class="q-name">Marcus E.</div><div class="q-role">Marketing Director at a SaaS Company</div>
  <p class="q-text">"Working with Brightvane.xyz is like having an in-house growth team. Their ability to create and optimize content-driven campaigns helped us double our inbound inquiries."</p></div>

<!-- cta -->
<div class="abs cta"></div>
<div class="abs" style="left:720px;top:4040px;width:259px;height:41px;background:var(--page);border-top-left-radius:18px"></div>
<div class="abs" style="left:938px;top:3998px;width:41px;height:44px;background:var(--page);border-top-left-radius:14px"></div>
<h2 class="abs heading h-section" style="left:263px;top:3831px;color:#fff;line-height:30px">Ready to Unlock<br>Scalable Growth for<br>Your Business?</h2>
<p class="abs body" style="left:263px;top:3940px;width:190px;color:#fff">Schedule a call to learn how we can help your business grow predictably and efficiently.</p>
<div class="abs" style="left:419px;top:3872px;width:218px;height:192px;background:radial-gradient(ellipse at 55% 50%,#4f9a2e 0%,#2f6a1c 35%,rgba(160,17,26,0) 70%)" role="img" aria-label="Illustration of a growth arrow made of green leaves"></div>
<div class="abs cta-list" style="left:657px;top:3832px;width:280px">
  <div class="title" style="font-size:9.5px;margin-bottom:20px">Our proven strategies are tailored to deliver</div>
  <div class="tick-item"><svg width="14" height="14" viewBox="0 0 16 16"><circle cx="8" cy="8" r="7" fill="none" stroke="#fff" stroke-width="1.2"/><path d="M5 8.2l2 2 4-4" fill="none" stroke="#fff" stroke-width="1.2"/></svg><p class="body">High-intent leads that match your ideal customer profile.</p></div>
  <div class="tick-item" style="margin-top:16px"><svg width="14" height="14" viewBox="0 0 16 16"><circle cx="8" cy="8" r="7" fill="none" stroke="#fff" stroke-width="1.2"/><path d="M5 8.2l2 2 4-4" fill="none" stroke="#fff" stroke-width="1.2"/></svg><p class="body">Custom campaigns designed to engage and convert your audience.</p></div>
  <div class="tick-item" style="margin-top:16px"><svg width="14" height="14" viewBox="0 0 16 16"><circle cx="8" cy="8" r="7" fill="none" stroke="#fff" stroke-width="1.2"/><path d="M5 8.2l2 2 4-4" fill="none" stroke="#fff" stroke-width="1.2"/></svg><p class="body">Actionable insights to optimize performance and scale effectively.</p></div>
</div>
<a class="abs pill pill-dark">Schedule your call now
  <span class="arrow-dot"><svg width="11" height="11" viewBox="0 0 12 12"><path d="M3 9L9 3M4 3h5v5" fill="none" stroke="#2e2e2e" stroke-width="1.3"/></svg></span></a>

<!-- footer -->
<div class="abs logo" style="left:0;top:4120px;font-size:20px">brightvane.xyz</div>
<p class="abs" style="left:0;width:1200px;text-align:center;top:4150px;font-size:8px;font-weight:500">Driving Real Growth, One Lead at a Time</p>
<p class="abs" style="left:0;width:1200px;text-align:center;top:4187px;font-size:7.5px;color:var(--muted)">Copyright 2025 Brightvane.xyz, LLC. All rights reserved.</p>
</body>
</html>
```